Brightpath Lingua Partners, LLC

We need a business card that includes information about our business and conveys a reliable business that provides document translation services and interpreters for a variety of corporate and individual clients. We want to come across as professional, reliable, yet approachable. It should include the following on one side:

ESL / ENL Language Classes, Private Lessons, and Online Tutors
PRELM Training and Testing
Translating & Interpreting Services
Contact us about Over-the-Phone Interpreting in over 200 languages
24/7/365
www.brightpathlingua.example

The other side should include (555) 418-2360

Reva Castillo, President
482 Larkmoor Ave., Ste. 213
Indianapolis, IN 40917

Please add USA as part of the address. Also, please add rmcastillo@brightpathlinguapartners.example as the e-mail address. Thank you.

Target Market(s)

Business professionals, their families, the international community

Industry/Entity Type

Business

Contact Information for Business Card

24/7/365
www.brightpathlingua.example

(555) 418-2360

Reva Castillo, President
482 Larkmoor Ave., Ste. 213
Indianapolis, IN 40917
USA

Font styles to use
Sans Serif

Colors

Designer to choose colors to be used in the design.

Requirements
Must have
• See project description
• e-mail address and web address
• Phone number
Nice to have
• a globe
• physical address
Should not have
• Should not have the same color scheme as other agencies in our market in Indiana unless it is blue and black. No purple or yellow.

```html
<!DOCTYPE html>
<html lang="en">
<head>
<meta charset="utf-8">
<title>Brightpath Lingua Partners — Business Card</title>
<link href="https://fonts.googleapis.com/css2?family=Lato:wght@400;700&display=swap" rel="stylesheet">
<style>
  :root {
    --ink: #0b0b0b;
    --paper: #ffffff;
    --brand-blue: #2394d3;
    --stage: #e9e9e9;
    --text-dark: #1a1a1a;
    --rule: #5a5a5a;
  }
  * { box-sizing: border-box; margin: 0; padding: 0; }
  html, body { width: 1200px; height: 900px; overflow: hidden; }
  body {
    background: var(--stage);
    font-family: "Lato", Arial, sans-serif;
    position: relative;
  }
  .card {
    position: absolute;
    left: 250px;
    width: 700px;
    height: 400px;
    overflow: hidden;
    box-shadow: 0 4px 14px rgba(0,0,0,0.18);
  }
  /* ---------- Back side ---------- */
  .card-back { top: 40px; background: var(--ink); color: var(--paper); }
  .back-brand {
    position: absolute; left: 40px; top: 70px; width: 180px;
    display: flex; flex-direction: column; align-items: center; gap: 18px;
  }
  .brand-dot {
    width: 120px; height: 120px; border-radius: 50%;
    background: var(--brand-blue); flex: none;
  }
  .back-brand .brand-name {
    font-size: 21px; font-weight: 700; color: var(--paper);
    text-align: center; line-height: 1.2;
  }
  .divider {
    position: absolute; left: 250px; top: 50px; width: 1px; height: 190px;
    background: linear-gradient(var(--ink), var(--rule) 30%, var(--rule) 70%, var(--ink));
  }
  .services {
    position: absolute; left: 280px; top: 60px; list-style: none;
    font-size: 17px; line-height: 1.6;
  }
  .services li { position: relative; padding-left: 18px; }
  .services li::before {
    content: ""; position: absolute; left: 0; top: 10px;
    width: 7px; height: 7px; border-radius: 50%; background: var(--brand-blue);
  }
  .availability {
    position: absolute; left: 330px; top: 268px;
    font-size: 27px; font-weight: 400;
  }
  .back-web {
    position: absolute; left: 230px; top: 318px;
    font-size: 27px; color: var(--brand-blue);
  }
  /* ---------- Front side ---------- */
  .card-front { top: 460px; background: var(--paper); color: var(--text-dark); }
  .wave { position: absolute; inset: 0; }
  .holder { position: absolute; left: 55px; top: 48px; }
  .holder-name {
    font-size: 26px; font-weight: 700; color: var(--brand-blue);
    letter-spacing: 0.5px; text-transform: uppercase;
  }
  .holder-title { font-size: 18px; margin-top: 4px; margin-left: 10px; }
  .front-brand {
    position: absolute; right: 40px; top: 38px;
    display: flex; align-items: center; gap: 14px;
  }
  .front-brand .brand-dot { width: 96px; height: 96px; }
  .front-brand .brand-name {
    font-size: 27px; font-weight: 400; color: var(--text-dark); line-height: 1.05;
  }
  .contact {
    position: absolute; left: 55px; top: 140px;
    font-size: 18px; line-height: 1.3; font-style: normal;
  }
  .contact-lines { list-style: none; margin-top: 10px; }
  .contact-lines li { display: flex; align-items: center; gap: 8px; }
  .icon { width: 16px; height: 16px; flex: none; }
</style>
</head>
<body>

<section class="card card-back" aria-label="Card back">
  <div class="back-brand">
    <span class="brand-dot"></span>
    <span class="brand-name">Brightpath Lingua Partners</span>
  </div>
  <span class="divider"></span>
  <ul class="services">
    <li>ESL / ENL Language Classes,</li>
    <li>Private Lessons, and Online Tutors</li>
    <li>PRELM Training and Testing</li>
    <li>Translating &amp; Interpreting Services</li>
    <li>Contact us about Over-the-Phone</li>
    <li>Interpreting in over 200 languages</li>
  </ul>
  <p class="availability">24/7/365</p>
  <p class="back-web">www.brightpathlingua.example</p>
</section>

<section class="card card-front" aria-label="Card front">
  <svg class="wave" viewBox="0 0 700 400" preserveAspectRatio="none" aria-hidden="true">
    <path d="M0,345 C220,335 440,300 700,150 L700,400 L0,400 Z" fill="var(--ink)"/>
    <path d="M0,318 C230,330 430,290 620,205 C440,308 220,346 0,346 Z" fill="var(--brand-blue)"/>
  </svg>

  <div class="holder">
    <p class="holder-name">Reva Castillo</p>
    <p class="holder-title">President</p>
  </div>

  <div class="front-brand">
    <span class="brand-dot"></span>
    <span class="brand-name">Brightpath<br>Lingua<br>Partners LLC</span>
  </div>

  <address class="contact">
    <p>482 Larkmoor Ave., Ste. 213</p>
    <p>Indianapolis, IN 40917 USA</p>
    <ul class="contact-lines">
      <li>
        <svg class="icon" viewBox="0 0 16 16" aria-hidden="true">
          <path d="M3 6 C3 3 13 3 13 6 L11 7 L10 5 L6 5 L5 7 Z M4 8 L12 8 L13 13 L3 13 Z" fill="var(--brand-blue)"/>
        </svg>
        (555) 418-2360
      </li>
      <li>
        <svg class="icon" viewBox="0 0 16 16" aria-hidden="true">
          <rect x="1" y="3" width="14" height="10" rx="1.5" fill="var(--brand-blue)"/>
          <path d="M1.5 4 L8 9 L14.5 4" stroke="var(--paper)" stroke-width="1.2" fill="none"/>
        </svg>
        rmcastillo@brightpathlinguapartners.example
      </li>
      <li>
        <svg class="icon" viewBox="0 0 16 16" aria-hidden="true">
          <circle cx="8" cy="8" r="7" fill="var(--brand-blue)"/>
          <path d="M1 8 H15 M8 1 C4 5 4 11 8 15 M8 1 C12 5 12 11 8 15" stroke="var(--paper)" stroke-width="1" fill="none"/>
        </svg>
        www.brightpathlingua.example
      </li>
    </ul>
  </address>
</section>

</body>
</html>
```